Brightwave Travel and Tours

Hotel Reservations
Airline Ticketing
Day Tour

My business is a Travel agency. My services are issuing domestic and international tickets. Book room/hotel reservations local/international.
My color preference is apple green/orange/red/blue.
Images of beaches, tickets,luggage.

```html
<!DOCTYPE html>
<html lang="en">
<head>
<meta charset="utf-8">
<title>Brightwave Travel and Tours – Business Card</title>
<link rel="stylesheet" href="https://fonts.googleapis.com/css2?family=Source+Sans+3:wght@400;600&display=swap">
<style>
  :root {
    --backdrop: #e9e7e2;
    --card: #ffffff;
    --teal: #138fae;
    --teal-deep: #0c7896;
    --cyan: #33c3e0;
    --ink-teal: #1b8aa8;
    --ink-soft: #4fb9d6;
    --ink-white: #ffffff;
  }
  * { box-sizing: border-box; margin: 0; padding: 0; }
  html, body { width: 1200px; height: 780px; overflow: hidden; }
  body {
    background: var(--backdrop);
    font-family: "Source Sans 3", sans-serif;
    display: flex;
    align-items: center;
    justify-content: center;
    gap: 40px;
  }
  .card {
    position: relative;
    width: 540px;
    height: 309px;
    background: var(--card);
    box-shadow: 0 6px 18px rgba(0,0,0,.18);
    overflow: hidden;
  }
  .card__waves { position: absolute; inset: 0; width: 100%; height: 100%; }

  .brand {
    position: absolute;
    display: flex;
    align-items: center;
    gap: 12px;
    color: var(--ink-teal);
    font-weight: 600;
    line-height: 1.05;
  }
  .brand__dot { flex: none; border-radius: 50%; background: var(--cyan); }
  .brand--front { left: 30px; top: 118px; font-size: 22px; }
  .brand--front .brand__dot { width: 46px; height: 46px; }
  .brand--back { left: 50%; top: 96px; transform: translateX(-50%); font-size: 28px; white-space: nowrap; }
  .brand--back .brand__dot { width: 58px; height: 58px; }
  .brand__sub { display: block; font-size: .62em; letter-spacing: .08em; text-transform: uppercase; }

  .holder {
    position: absolute;
    right: 30px;
    top: 22px;
    text-align: right;
    line-height: 1.15;
  }
  .holder__name { color: var(--ink-teal); font-size: 24px; font-weight: 600; }
  .holder__role { color: var(--ink-soft); font-size: 15px; }

  .contact {
    position: absolute;
    right: 26px;
    bottom: 22px;
    list-style: none;
    color: var(--ink-white);
    font-size: 13px;
    line-height: 1.6;
    text-align: right;
  }
  .contact li { display: flex; justify-content: flex-end; align-items: center; gap: 8px; }
  .contact svg { width: 13px; height: 13px; flex: none; }

  .services {
    position: absolute;
    left: 0; right: 0;
    top: 196px;
    text-align: center;
    color: var(--ink-teal);
    font-size: 17px;
  }
</style>
</head>
<body>

  <section class="card card--front">
    <svg class="card__waves" viewBox="0 0 540 309" aria-hidden="true">
      <path d="M95 309 C210 300 270 238 302 176 C336 112 410 86 540 82 L540 309 Z" fill="var(--cyan)"/>
      <path d="M128 309 C235 298 292 236 322 180 C354 120 425 100 540 98 L540 309 Z" fill="var(--teal)"/>
      <path d="M150 309 C250 292 292 240 318 196" fill="none" stroke="#ffffff" stroke-width="3" opacity=".85"/>
      <path d="M175 309 C272 296 318 238 348 186 C378 136 440 118 540 114 L540 309 Z" fill="var(--teal-deep)" opacity=".3"/>
    </svg>

    <div class="brand brand--front">
      <span class="brand__dot"></span>
      <span>Brightwave<span class="brand__sub">Travel and Tours</span></span>
    </div>

    <div class="holder">
      <div class="holder__name">Employee Name</div>
      <div class="holder__role">Managing Director</div>
    </div>

    <ul class="contact">
      <li>000 000 0000
        <svg viewBox="0 0 16 16"><path d="M4 1.5l2.4 3-1.4 1.6c.8 1.9 2.3 3.4 4.2 4.2l1.6-1.4 3 2.4-1.6 2.4C7.4 13.5 2.5 8.6 1.6 3.1z" fill="#fff"/></svg>
      </li>
      <li>info@youremail.co.nz
        <svg viewBox="0 0 16 16"><rect x="1.5" y="3.5" width="13" height="9" fill="none" stroke="#fff" stroke-width="1.4"/><path d="M1.5 3.5L8 9l6.5-5.5" fill="none" stroke="#fff" stroke-width="1.4"/></svg>
      </li>
      <li>www.yourwebsite.com
        <svg viewBox="0 0 16 16"><circle cx="8" cy="8" r="6.3" fill="none" stroke="#fff" stroke-width="1.4"/><ellipse cx="8" cy="8" rx="2.6" ry="6.3" fill="none" stroke="#fff" stroke-width="1.2"/><path d="M1.7 8h12.6" stroke="#fff" stroke-width="1.2"/></svg>
      </li>
      <li>your address Rd., Suite 000, Harborview, USA</li>
    </ul>
  </section>

  <section class="card card--back">
    <div class="brand brand--back">
      <span class="brand__dot"></span>
      <span>Brightwave<span class="brand__sub">Travel and Tours</span></span>
    </div>
    <p class="services">Hotel Reservations | Airline Ticketing | Day Tour</p>
  </section>

</body>
</html>
```